Ecommerce Web Design - We currently have a live website running on https://www.plovenrik.co.za - this website must be redesigned for an eCommerce website since we are moving to sell our items online. Kindly put a new design utilising the information from the current live website

Link to Pictures & Brochure: https://dostravel-files.example.com/:f:/g/personal/tavimo_rushe_co_za/QxxLPTmvdJaUkrBWa7TYzpfnC-KLM9dHWuqTXCB4jLNUwe?e=qR5m31

```html
<!DOCTYPE html>
<html lang="en">
<head>
<meta charset="utf-8">
<title>Plovenrik Ladders – Shop</title>
<link href="https://fonts.googleapis.com/css2?family=Rubik:wght@400;500;600;700&family=DM+Sans:wght@400;500;700&display=swap" rel="stylesheet">
<style>
:root{
  --navy:#0f2c7e;
  --red:#d7263d;
  --green:#2f8f3f;
  --ink:#1d1d24;
  --muted:#6b6f7b;
  --soft:#f2f2f4;
  --star:#f5b700;
  --white:#ffffff;
}
*{box-sizing:border-box;margin:0;padding:0}
html,body{width:1200px;height:4528px;overflow:hidden}
body{font-family:"DM Sans",sans-serif;color:var(--ink);background:var(--white);position:relative}
h1,h2,h3,h4,h5{font-family:"Rubik",sans-serif}
svg{display:block}

.topbar{position:absolute;top:0;left:0;width:1200px;height:28px;background:#ececee;font-size:11px;color:#444}
.topbar .item{position:absolute;top:7px;display:flex;align-items:center;gap:6px;white-space:nowrap}
.topbar a{color:#777;font-size:10px;text-decoration:underline}

.header{position:absolute;top:28px;left:0;width:1200px;height:72px}
.brand{position:absolute;left:58px;top:10px;display:flex;align-items:center;gap:10px}
.brand .mark{width:50px;height:50px;background:var(--navy)}
.brand .name{font-family:"Rubik",sans-serif;font-weight:600;font-size:14px;line-height:18px;color:var(--ink)}
.head-tools{position:absolute;right:58px;top:16px;display:flex;gap:28px}
.tool{display:flex;align-items:center;gap:8px;font-size:11px;line-height:13px}
.tool b{color:var(--navy);font-weight:700}
.tool span{color:var(--muted);font-size:9px;display:block}

.nav{position:absolute;top:100px;left:0;width:1200px;height:80px;background:var(--navy);border-bottom:4px solid var(--red)}
.nav ul{position:absolute;left:58px;top:29px;display:flex;gap:36px;list-style:none}
.nav li{color:#fff;font-family:"Rubik",sans-serif;font-weight:500;font-size:16px}
.search{position:absolute;right:58px;top:19px;width:395px;height:40px;background:#fff;border-radius:3px;font-size:11px;color:#555;padding:13px 14px}
.search svg{position:absolute;right:12px;top:11px}

.hero{position:absolute;top:180px;left:0;width:1200px;height:457px;background:linear-gradient(100deg,#1c2026 0%,#35383c 45%,#5b5650 75%,#3a3c40 100%)}
.hero h1{position:absolute;left:58px;top:80px;color:#fff;font-weight:600;font-size:34px;line-height:53px;white-space:nowrap}
.hero p{position:absolute;left:58px;top:246px;color:#fff;font-size:15px;line-height:27px}
.btn{display:inline-block;font-family:"Rubik",sans-serif;font-weight:500;font-size:15px;border-radius:3px}
.btn-navy{background:var(--navy);color:#fff}
.hero .btn{position:absolute;left:58px;top:328px;width:147px;height:48px;line-height:48px;text-align:center}

.signin{position:absolute;top:670px;left:0;width:1200px;height:78px;background:var(--soft)}
.signin h3{position:absolute;left:58px;top:29px;font-weight:500;font-size:17px;color:#333}
.signin .a{position:absolute;top:19px;height:40px;line-height:40px;text-align:center;font-size:13px;border-radius:3px}

.sec-title{position:absolute;left:58px;border-left:4px solid var(--navy);padding-left:10px;font-weight:500;font-size:28px;line-height:34px;color:var(--ink);white-space:nowrap}
.sec-title em{font-style:normal;color:var(--navy)}

.chips{position:absolute;left:58px;top:896px;display:flex;gap:12px}
.chip{height:26px;line-height:26px;padding:0 14px;font-size:11px;color:#666;background:#f0f0f2;border-radius:3px;white-space:nowrap}
.chip.on{background:var(--navy);color:#fff}

.card{position:absolute;width:258px}
.card .shot{position:relative;height:354px;border-radius:4px;background:linear-gradient(180deg,#f3f3f5,#e6e7ea)}
.badge{position:absolute;left:14px;top:14px;width:52px;height:52px;border-radius:50%}
.b-gold{background:#f2c11d}.b-blue{background:#3d8fd8}.b-red{background:#d7263d}
.heart{position:absolute;right:14px;top:14px}
.add{position:absolute;left:14px;bottom:18px;background:var(--green);color:#fff;font-size:11px;padding:6px 10px;border-radius:3px}
.price{font-family:"Rubik",sans-serif;font-weight:600;font-size:17px;margin-top:12px;color:var(--ink)}
.pname{font-size:12px;margin-top:6px;color:#333;white-space:nowrap}
.stars{margin-top:6px}

.center-btn{position:absolute;left:481px;top:1910px;width:238px;height:48px;line-height:48px;text-align:center}

.about{position:absolute;top:2030px;left:0;width:1200px;height:530px;background:var(--soft)}
.about .txt{position:absolute;left:58px;top:156px;width:540px;font-size:16px;line-height:23px;color:#333}
.about .outline{position:absolute;left:58px;top:405px;width:129px;height:43px;line-height:41px;text-align:center;border:1.5px solid var(--navy);color:var(--navy);border-radius:3px;font-size:14px;background:#fff}
.about .photo{position:absolute;left:679px;top:64px;width:462px;height:403px;background:linear-gradient(160deg,#dfe5ea 0%,#9aa6b0 40%,#5f8a3a 75%,#7cb342 100%)}

.cats{position:absolute;top:2712px;left:58px;width:1084px;display:flex;justify-content:space-between}
.cat{width:133px;text-align:center}
.cat .circle{width:133px;height:133px;border-radius:50%;background:#fff;box-shadow:0 4px 16px rgba(0,0,0,.1);display:flex;align-items:center;justify-content:center}
.cat.on .circle{background:var(--navy)}
.cat .label{font-family:"Rubik",sans-serif;font-weight:500;font-size:16px;line-height:18px;margin-top:14px;color:#333}
.cat.on .label{color:var(--navy)}

.scard{position:absolute;top:3050px;width:350px}
.scard .shot{position:relative;height:255px;border-radius:4px;background:linear-gradient(180deg,#f6f6f7 0%,#e9e7e3 65%,#d8d2c6 100%)}
.scard .add{left:auto;right:16px}
.old{color:#999;text-decoration:line-through;margin-right:10px}
.new{color:var(--green)}

.deliver{position:absolute;top:3465px;left:58px;width:1084px;height:106px;border:1.5px solid var(--navy);background:#fff}
.deliver .brand{left:22px;top:24px}
.deliver .brand .mark{width:54px;height:54px}
.deliver h3{position:absolute;left:0;right:0;top:20px;text-align:center;font-weight:600;font-size:20px}
.deliver h3 em{font-style:normal;color:var(--navy)}
.deliver p{position:absolute;left:230px;width:620px;top:52px;text-align:center;font-size:11px;line-height:22px;color:#333}
.deliver .btn{position:absolute;right:22px;top:28px;width:147px;height:50px;line-height:50px;text-align:center}

.features{position:absolute;top:3640px;left:0;width:1200px;height:190px;background:var(--soft)}
.feat{position:absolute;top:40px;display:flex;gap:14px}
.feat h4{font-weight:500;font-size:17px;line-height:22px;color:var(--navy)}
.feat p{font-size:11px;line-height:16px;color:#333;margin-top:8px;width:138px}
.feat a{color:var(--navy);font-size:11px;text-decoration:underline}

.promo{position:absolute;top:3915px;left:58px;width:621px;height:230px;background:linear-gradient(90deg,#3f6b2c 0%,#8fa77f 30%,#d9d4c8 60%,#c9b08a 100%)}
.promo .tag{position:absolute;left:20px;top:18px;background:var(--navy);color:#fff;font-family:"Rubik",sans-serif;font-weight:500;font-size:19px;padding:8px 16px;border:2px solid #fff}
.promo .off{position:absolute;left:20px;top:92px;color:#fff;font-family:"Rubik",sans-serif;font-weight:700;font-size:26px}
.promo .sub{position:absolute;left:20px;top:130px;color:#fff;font-size:11px;line-height:13px;width:140px}
.map{position:absolute;top:3915px;left:703px;width:438px;height:230px;background:linear-gradient(135deg,#eef1e9 0%,#e3e8dc 50%,#dfe6ea 100%)}
.map .dir{position:absolute;right:16px;bottom:26px;width:168px;height:44px;background:var(--navy);color:#fff;border:2px solid #fff;border-radius:4px;display:flex;align-items:center;justify-content:center;gap:8px;font-family:"Rubik",sans-serif;font-weight:500;font-size:16px}

.footer{position:absolute;top:4225px;left:0;width:1200px;height:303px;background:#f7f7f8}
.footer .brand{left:100px;top:36px}
.footer .about-f{position:absolute;left:100px;top:135px;width:250px;font-size:13px;line-height:23px;color:#333}
.fcol{position:absolute;top:60px;font-size:13px;line-height:23px;color:#555;white-space:nowrap}
.fcol h5{font-weight:500;font-size:15px;color:var(--navy);margin-bottom:14px}
.vline{position:absolute;top:102px;height:110px;width:1px;background:#c8c8cc}
.socials{display:flex;gap:12px;margin-top:10px}
.socials i{width:20px;height:20px;background:var(--navy);border-radius:4px;display:block}
.copy{position:absolute;left:58px;right:58px;top:4505px;border-top:1px solid #9a9aa0;padding-top:6px;font-size:12px;color:#555}
.copy .links{position:absolute;right:40px;top:6px}
</style>
</head>
<body>
<svg width="0" height="0" style="position:absolute"><defs><path id="s" d="M7 0l2 4.6 5 .5-3.8 3.3 1.2 5L7 10.8 2.6 13.4l1.2-5L0 5.1l5-.5z"/><path id="h" d="M12 20s-9-5.6-9-11.5A5 5 0 0 1 12 6a5 5 0 0 1 9 2.5C21 14.4 12 20 12 20z"/><g id="st" fill="#f5b700"><use href="#s"/><use href="#s" x="19"/><use href="#s" x="38"/><use href="#s" x="57"/><use href="#s" x="76"/></g></defs></svg>

<div class="topbar">
  <div class="item" style="left:58px">
    <svg width="12" height="12" viewBox="0 0 24 24"><path d="M6.6 10.8a15 15 0 0 0 6.6 6.6l2.2-2.2a1 1 0 0 1 1-.25 11.4 11.4 0 0 0 3.6.57 1 1 0 0 1 1 1V20a1 1 0 0 1-1 1A17 17 0 0 1 3 4a1 1 0 0 1 1-1h3.5a1 1 0 0 1 1 1c0 1.25.2 2.45.57 3.57a1 1 0 0 1-.25 1z" fill="#0f2c7e"/></svg>
    +27-11-555-0142
  </div>
  <div class="item" style="left:218px">
    <svg width="13" height="10" viewBox="0 0 26 20"><rect width="26" height="20" rx="2" fill="#0f2c7e"/><path d="M2 3l11 8 11-8" stroke="#fff" stroke-width="2" fill="none"/></svg>
    contact@plovenriks.co.za
  </div>
  <div class="item" style="right:58px">We Deliver All Across South Africa. <a>Learn more</a></div>
</div>

<header class="header">
  <div class="brand"><div class="mark"></div><div class="name">PLOVENRIK<br>LADDERS</div></div>
  <div class="head-tools">
    <div class="tool">
      <svg width="34" height="30" viewBox="0 0 24 22"><use href="#h" fill="none" stroke="#1d1d24" stroke-width="1.6"/><circle cx="4" cy="3" r="3" fill="#d7263d"/></svg>
      <div><b>Favorites</b><span>01 items</span></div>
    </div>
    <div class="tool">
      <svg width="34" height="30" viewBox="0 0 24 22"><path d="M2 4h3l2.5 11h11L21 7H6.5" fill="none" stroke="#1d1d24" stroke-width="1.6"/><circle cx="9" cy="19" r="1.6" fill="#1d1d24"/><circle cx="17" cy="19" r="1.6" fill="#1d1d24"/><circle cx="4" cy="3" r="3" fill="#d7263d"/></svg>
      <div><b>Your Cart</b><span>0 items</span></div>
    </div>
    <div class="tool">
      <svg width="32" height="32" viewBox="0 0 24 24"><circle cx="12" cy="12" r="10.5" fill="none" stroke="#1d1d24" stroke-width="1.6"/><circle cx="12" cy="10" r="3.5" fill="none" stroke="#1d1d24" stroke-width="1.6"/><path d="M5.5 19a7 7 0 0 1 13 0" fill="none" stroke="#1d1d24" stroke-width="1.6"/></svg>
      <div><b>Welcome!</b><span>Sign Up | Log In</span></div>
    </div>
  </div>
</header>

<nav class="nav">
  <ul><li>Home</li><li>Products</li><li>Categories</li><li>Downloads</li><li>About Us</li></ul>
  <div class="search">What Are You Looking For Today ?
    <svg width="18" height="18" viewBox="0 0 24 24"><circle cx="10" cy="10" r="7" fill="none" stroke="#333" stroke-width="2"/><path d="M15 15l6 6" stroke="#333" stroke-width="2"/></svg>
  </div>
</nav>

<section class="hero" role="img" aria-label="Worker on a step ladder fitting a ceiling in a room under construction">
  <h1>South Africa Leading<br>Manufacturer Of Ladders, Trolleys,<br>Casters, and Ladder Accessories</h1>
  <p>Welcome To the Ladder Shop, We Cover<br>All Types Of Ladders</p>
  <a class="btn btn-navy">Shop Now</a>
</section>

<section class="signin">
  <h3>SING IN AND LET US TAKE CARE OF ALL YOUR LADDERS NEEDS.</h3>
  <a class="a" style="left:882px;width:96px;background:var(--navy);color:#fff">Sign In</a>
  <a class="a" style="left:991px;width:151px;border:1.5px solid var(--navy);color:var(--navy);background:#fff">Create Account</a>
</section>

<h2 class="sec-title" style="top:830px">Discover Our Featured <em>Products</em></h2>
<div class="chips">
  <span class="chip on">All</span><span class="chip">Access Equipements</span><span class="chip">Alluminium Ladders</span><span class="chip">Castor Wheels</span><span class="chip">Fiberglass Ladders</span><span class="chip">Ladders Accessories</span><span class="chip">Storage Equipements</span><span class="chip">Trolleys</span>
  <span class="chip" style="padding:0 8px"><svg width="16" height="26" viewBox="0 0 16 26"><path d="M2 10h5M10 10h4M2 16h3M8 16h6" stroke="#555" stroke-width="2"/></svg></span>
</div>

<div class="card" style="left:58px;top:986px">
  <div class="shot" role="img" aria-label="Aluminium multipurpose ladder"><i class="badge b-blue"></i>
    <svg class="heart" width="22" height="20" viewBox="0 0 24 22"><use href="#h" fill="#cfd0d4"/></svg><span class="add">+ Add</span></div>
  <div class="price">2200 R</div><div class="pname">TR Range Ladder</div>
  <svg class="stars" width="90" height="14"><use href="#st"/></svg>
</div>
<div class="card" style="left:333px;top:986px">
  <div class="shot" role="img" aria-label="Yellow fibreglass step ladder"><i class="badge b-gold"></i>
    <svg class="heart" width="22" height="20" viewBox="0 0 24 22"><use href="#h" fill="#d7263d"/></svg><span class="add">+ Add</span></div>
  <div class="price">3500 R</div><div class="pname">720 Range Ladder - 016</div>
  <svg class="stars" width="90" height="14"><use href="#st"/></svg>
</div>
<div class="card" style="left:608px;top:986px">
  <div class="shot" role="img" aria-label="Red fibreglass step ladder"><i class="badge b-blue"></i>
    <svg class="heart" width="22" height="20" viewBox="0 0 24 22"><use href="#h" fill="#cfd0d4"/></svg><span class="add">+ Add</span></div>
  <div class="price">3745 R</div><div class="pname">KVR Range Ladder - 016</div>
  <svg class="stars" width="90" height="14"><use href="#st"/></svg>
</div>
<div class="card" style="left:883px;top:986px">
  <div class="shot" role="img" aria-label="Aluminium step ladder with yellow top"><i class="badge b-gold"></i>
    <svg class="heart" width="22" height="20" viewBox="0 0 24 22"><use href="#h" fill="#cfd0d4"/></svg><span class="add">+ Add</span></div>
  <div class="price">4750 R</div><div class="pname">DPL Range Ladder - 016</div>
  <svg class="stars" width="90" height="14"><use href="#st"/></svg>
</div>

<div class="card" style="left:58px;top:1448px">
  <div class="shot" role="img" aria-label="Yellow fibreglass folding combination ladder"><i class="badge b-gold"></i>
    <svg class="heart" width="22" height="20" viewBox="0 0 24 22"><use href="#h" fill="#cfd0d4"/></svg><span class="add">+ Add</span></div>
  <div class="price">3745 R</div><div class="pname">HXMT 4120 - Fold Ladder</div>
  <svg class="stars" width="90" height="14"><use href="#st"/></svg>
</div>
<div class="card" style="left:333px;top:1448px">
  <div class="shot" role="img" aria-label="Aluminium step ladder"><i class="badge b-gold"></i>
    <svg class="heart" width="22" height="20" viewBox="0 0 24 22"><use href="#h" fill="#cfd0d4"/></svg><span class="add">+ Add</span></div>
  <div class="price">2250 R</div><div class="pname">DPL Range Ladder - 015</div>
  <svg class="stars" width="90" height="14"><use href="#st"/></svg>
</div>
<div class="card" style="left:608px;top:1448px">
  <div class="shot" role="img" aria-label="Aluminium platform step ladder"><i class="badge b-gold"></i>
    <svg class="heart" width="22" height="20" viewBox="0 0 24 22"><use href="#h" fill="#cfd0d4"/></svg><span class="add">+ Add</span></div>
  <div class="price">2675 R</div><div class="pname">DPL Range Ladder - 014</div>
  <svg class="stars" width="90" height="14"><use href="#st"/></svg>
</div>
<div class="card" style="left:883px;top:1448px">
  <div class="shot" role="img" aria-label="Red fibreglass extension ladder"><i class="badge b-blue"></i>
    <svg class="heart" width="22" height="20" viewBox="0 0 24 22"><use href="#h" fill="#cfd0d4"/></svg><span class="add">+ Add</span></div>
  <div class="price">1980 R</div><div class="pname">460 Series - Fiberglass Extention</div>
  <svg class="stars" width="90" height="14"><use href="#st"/></svg>
</div>

<a class="btn btn-navy center-btn">Discover All Products</a>

<section class="about">
  <h2 class="sec-title" style="top:84px">What You Need To Know <em>About Us</em></h2>
  <div class="txt">
    Plovenrik Ladders was founded in 1992 as a family owned manufacturing business that produces ladders. Today, we have evolved to a business that manufactures ladders, trolleys, castors, wheels, store bins, scaffolding and ladder accessories for Southern Africa and international markets.<br>
    We are a proudly South African company with a local manufacturing footprint.<br>
    All our ladder ranges, both Aluminium and Fibreglass have been tested in accordance &nbsp;with SANS 5.131-1, 2, 3 and ...
  </div>
  <a class="outline">Read More</a>
  <div class="photo" role="img" aria-label="Workers on ladders installing green panels on a building wall"></div>
</section>

<h2 class="sec-title" style="top:2620px">Shop By &nbsp;<em>Categories</em></h2>
<div class="cats">
  <div class="cat"><div class="circle"><svg width="70" height="80" viewBox="0 0 70 80" fill="none" stroke="#0f2c7e" stroke-width="3"><path d="M40 6L18 66M52 6L34 66M36 18h14M32 30h14M28 42h14M24 54h14M18 66h40"/><circle cx="20" cy="72" r="5"/><circle cx="54" cy="72" r="5"/></svg></div><div class="label">Access<br>Equipement</div></div>
  <div class="cat on"><div class="circle"><svg width="70" height="80" viewBox="0 0 70 80" fill="none" stroke="#fff" stroke-width="3"><path d="M22 6h26M24 6L10 74M46 6l14 68M30 6L22 74M40 6l8 68M18 30h34M16 46h38M13 62h44"/></svg></div><div class="label">Aluminium<br>Ladders</div></div>
  <div class="cat"><div class="circle"><svg width="40" height="80" viewBox="0 0 40 80" fill="none" stroke="#0f2c7e" stroke-width="3"><path d="M10 4v72M30 4v72M10 16h20M10 30h20M10 44h20M10 58h20"/></svg></div><div class="label">Fiberglass<br>Ladders</div></div>
  <div class="cat"><div class="circle"><svg width="70" height="80" viewBox="0 0 70 80" fill="none" stroke="#0f2c7e" stroke-width="3"><path d="M18 8h34v8H18zM30 16v14h10V16"/><path d="M35 30c-12 0-18 10-18 20"/><circle cx="40" cy="56" r="16"/><circle cx="40" cy="56" r="6"/></svg></div><div class="label">Caster<br>Wheels</div></div>
  <div class="cat"><div class="circle"><svg width="80" height="70" viewBox="0 0 80 70" fill="none" stroke="#0f2c7e" stroke-width="3"><path d="M10 20h60v42H10zM10 34h60M16 20l6-12h36l6 12M30 46h20v8H30z"/></svg></div><div class="label">Storage<br>Equipement</div></div>
  <div class="cat"><div class="circle"><svg width="70" height="80" viewBox="0 0 70 80" fill="none" stroke="#0f2c7e" stroke-width="3"><path d="M20 8h30v8H20zM22 16L12 74M48 16l10 58M30 16v58M40 16v58M16 40h38M14 58h42"/></svg></div><div class="label">Ladders<br>Accessories</div></div>
  <div class="cat"><div class="circle"><svg width="70" height="80" viewBox="0 0 70 80" fill="none" stroke="#0f2c7e" stroke-width="3"><path d="M8 6h10l20 52h24"/><path d="M26 22l22-8 10 26-22 8z"/><circle cx="36" cy="66" r="6"/></svg></div><div class="label">Trolleys</div></div>
</div>

<h2 class="sec-title" style="top:2981px">See What <em>Savings</em> Are Available</h2>
<div class="scard" style="left:58px">
  <div class="shot" role="img" aria-label="Yellow fibreglass step ladder on a wooden floor"><i class="badge b-gold"></i>
    <svg class="heart" width="22" height="20" viewBox="0 0 24 22"><use href="#h" fill="#cfd0d4"/></svg><span class="add">+ Add</span></div>
  <div class="price"><span class="old">3500R</span><span class="new">3200 R</span></div><div class="pname">720 Range Ladder - 016</div>
  <svg class="stars" width="90" height="14"><use href="#st"/></svg>
</div>
<div class="scard" style="left:425px">
  <div class="shot" role="img" aria-label="Red fibreglass step ladder on a wooden floor"><i class="badge b-red"></i>
    <svg class="heart" width="22" height="20" viewBox="0 0 24 22"><use href="#h" fill="#cfd0d4"/></svg><span class="add">+ Add</span></div>
  <div class="price"><span class="old">3745 R</span><span class="new">3200 R</span></div><div class="pname">KVR Range Ladder - 016</div>
  <svg class="stars" width="90" height="14"><use href="#st"/></svg>
</div>
<div class="scard" style="left:792px">
  <div class="shot" role="img" aria-label="Aluminium step ladder on a wooden floor"><i class="badge b-gold"></i>
    <svg class="heart" width="22" height="20" viewBox="0 0 24 22"><use href="#h" fill="#cfd0d4"/></svg><span class="add">+ Add</span></div>
  <div class="price"><span class="old">2250 R</span><span class="new">3200 R</span></div><div class="pname">DPL Range Ladder - 015</div>
  <svg class="stars" width="90" height="14"><use href="#st"/></svg>
</div>

<section class="deliver">
  <div class="brand"><div class="mark"></div><div class="name">PLOVENRIK<br>LADDERS</div></div>
  <h3>WE DELIVER ACROSS ALL <em>SOUTH AFRICA</em></h3>
  <p>All Customers are currently serviced from our Johannesburg Head Office. Delivery anywhere in South Africa can be arranged at a cost and for the customers own account and preferred courier service</p>
  <a class="btn btn-navy">Shop Now</a>
</section>

<section class="features">
  <div class="feat" style="left:60px">
    <svg width="76" height="60" viewBox="0 0 76 60" fill="none" stroke="#0f2c7e" stroke-width="2.5"><path d="M14 40a24 24 0 0 1 48 0M26 18v20M38 14v24M50 18v20M4 40h68v10H4z"/></svg>
    <div><h4>Your Safety is<br>Our Concern</h4><p>all our ranges are duly rated from household to extra heavy duty to ensure your safety</p></div>
  </div>
  <div class="feat" style="left:340px">
    <svg width="76" height="70" viewBox="0 0 76 70" fill="none" stroke="#0f2c7e" stroke-width="2.5"><path d="M4 18L30 6l26 12v30L30 60 4 48zM4 18l26 12 26-12M30 30v30"/><circle cx="54" cy="46" r="14" fill="#fff"/><path d="M54 38v8l6 4"/></svg>
    <div><h4>We Deliver<br>Country Wide</h4><p>All Customers are currently serviced from our Johannesburg Head Office.</p></div>
  </div>
  <div class="feat" style="left:644px">
    <svg width="60" height="70" viewBox="0 0 60 70" fill="none" stroke="#0f2c7e" stroke-width="2.5"><path d="M12 4h40v56H12zM4 12v56h40"/><path d="M20 16h8v8h-8zM34 18h12M20 32h8v8h-8zM34 34h12M20 48h24"/></svg>
    <div><h4>Products<br>Catalogue</h4><p>full product cataogue as a pdf download.</p><a>⤓ Download Here</a></div>
  </div>
  <div class="feat" style="left:910px;top:32px">
    <svg width="76" height="76" viewBox="0 0 76 76" fill="none" stroke="#0f2c7e" stroke-width="2.5"><path d="M34 4h36v24H46l-8 8v-8h-4z"/><path d="M42 12h20M42 20h14"/><circle cx="28" cy="40" r="9"/><path d="M10 70c0-12 8-20 18-20s18 8 18 20"/></svg>
    <div><h4>Professional's<br>Advice</h4><p style="width:120px">For a professional's advice call us.</p><a>+27-11-555-0142</a></div>
  </div>
</section>

<section class="promo" role="img" aria-label="Red and yellow fibreglass step ladders on a wooden floor with a green garden backdrop">
  <div class="tag">Fiberglass Range</div>
  <div class="off">10% OFF</div>
  <div class="sub">Purchase Your New Fiberglass Ladder Now</div>
</section>
<section class="map" role="img" aria-label="Street map of northern Johannesburg showing the showroom location">
  <a class="dir"><svg width="20" height="20" viewBox="0 0 24 24"><rect x="4" y="4" width="16" height="16" transform="rotate(45 12 12)" fill="#fff"/><path d="M9 14v-3h5M12 9l2 2-2 2" stroke="#0f2c7e" stroke-width="2" fill="none"/></svg>Directions</a>
</section>

<footer class="footer">
  <div class="brand"><div class="mark" style="width:58px;height:58px"></div><div class="name">PLOVENRIK<br>LADDERS</div></div>
  <div class="about-f">From Step Ladders To Extention Ladders, Platform Ladders, Trolleys To Order Pickers And Everything In Between.</div>
  <div class="fcol" style="left:472px"><h5>Browse</h5>Home<br>Products<br>Safety<br>Categories<br>Delivery</div>
  <div class="vline" style="left:604px"></div>
  <div class="fcol" style="left:657px"><h5>Customer Service</h5>Take Your Order<br>Easy Returns<br>Shipping &amp; Pickup<br>Warranty<br>Services</div>
  <div class="vline" style="left:855px"></div>
  <div class="fcol" style="left:907px"><h5>Contact Us</h5>
    <div style="display:flex;align-items:center;gap:6px"><svg width="12" height="12" viewBox="0 0 24 24"><path d="M6.6 10.8a15 15 0 0 0 6.6 6.6l2.2-2.2a1 1 0 0 1 1-.25 11.4 11.4 0 0 0 3.6.57 1 1 0 0 1 1 1V20a1 1 0 0 1-1 1A17 17 0 0 1 3 4a1 1 0 0 1 1-1h3.5a1 1 0 0 1 1 1c0 1.25.2 2.45.57 3.57a1 1 0 0 1-.25 1z" fill="#1d1d24"/></svg>+27 11 555 0142</div>
    <div style="display:flex;align-items:center;gap:6px"><svg width="12" height="10" viewBox="0 0 26 20"><rect width="26" height="20" rx="2" fill="#1d1d24"/><path d="M2 3l11 8 11-8" stroke="#fff" stroke-width="2" fill="none"/></svg>contact@plovenriks.co.za</div>
    <div style="font-family:Rubik,sans-serif;font-weight:500;font-size:15px;color:var(--ink);margin-top:14px">Follow Us</div>
    <div class="socials"><i></i><i></i><i></i><i></i></div>
  </div>
</footer>
<div class="copy">© copyrighted, Plovenrik ladders. 2022
  <span class="links">Return Policy &nbsp;|&nbsp; Privacy Policy &nbsp;|&nbsp; Terms &amp; Conditions</span>
</div>

</body>
</html>
```